Business Card Design

Business Card for professional consulting firm working with large financial institutions.

Target Market(s)

Executive buyers

Industry/Entity Type

Banking

Contact Information for Business Card

Mild creativity wanted. Not boring, but do elaborate artwork.

Font styles to use
Serif
Sans Serif

Colors

Designer to choose colors to be used in the design.

Requirements
Must have
• Standard business card features - company name, individual name, telephone, website, email, locations.
Nice to have
• Two colors
Should not have
• too many colors, fancy printing, cartoons.

```html
<!DOCTYPE html>
<html lang="en">
<head>
<meta charset="utf-8">
<title>Quorvane Advisory — Business Card</title>
<link rel="stylesheet" href="https://fonts.googleapis.com/css2?family=Roboto+Slab:wght@400;700&family=Roboto:wght@400&display=swap">
<style>
  :root {
    --backdrop: #d8d8d8;
    --paper: #f4f4f4;
    --ink: #000000;
    --ink-soft: #3a3a3a;
    --muted: #555555;
    --on-dark: #ffffff;
  }
  * { margin: 0; padding: 0; box-sizing: border-box; }
  html, body {
    width: 1200px;
    height: 960px;
    overflow: hidden;
    background: var(--backdrop);
  }
  .canvas {
    position: relative;
    width: 1200px;
    height: 960px;
  }
  .card {
    position: absolute;
    width: 601px;
    height: 343px;
  }
  .brand {
    display: flex;
    align-items: center;
    gap: 10px;
    font-family: "Roboto Slab", Georgia, serif;
    font-weight: 400;
    white-space: nowrap;
  }
  .brand__dot {
    width: 10px;
    height: 10px;
    border-radius: 50%;
    background: currentColor;
  }
  /* Front */
  .card--front {
    left: 314px;
    top: 113px;
    background: var(--paper);
  }
  .card--front .brand {
    position: absolute;
    left: 100px;
    top: 70px;
    font-size: 28px;
    line-height: 34px;
    color: var(--ink-soft);
  }
  .identity-band {
    position: absolute;
    left: 0;
    top: 186px;
    width: 100%;
    height: 109px;
    background: var(--ink);
    color: var(--on-dark);
  }
  .person {
    position: absolute;
    left: 53px;
    top: 32px;
    font-family: "Roboto Slab", Georgia, serif;
  }
  .person__name {
    font-size: 20px;
    font-weight: 700;
    letter-spacing: 0.3px;
    line-height: 26px;
  }
  .person__title {
    font-size: 14px;
    font-weight: 400;
    letter-spacing: 0.3px;
    line-height: 18px;
  }
  .contacts {
    position: absolute;
    left: 377px;
    top: 26px;
    list-style: none;
    font-family: "Roboto", Arial, sans-serif;
    font-size: 14px;
    line-height: 19px;
  }
  .contacts__item {
    display: flex;
    align-items: center;
    gap: 8px;
  }
  .contacts__icon {
    width: 13px;
    height: 13px;
    fill: var(--on-dark);
  }
  .address {
    position: absolute;
    left: 52px;
    top: 306px;
    font-family: "Roboto", Arial, sans-serif;
    font-size: 14px;
    color: var(--muted);
  }
  /* Back */
  .card--back {
    left: 311px;
    top: 472px;
    width: 600px;
    background: var(--ink);
    display: flex;
    align-items: center;
    justify-content: center;
  }
  .card--back .brand {
    font-size: 33px;
    color: var(--on-dark);
  }
</style>
</head>
<body>
<main class="canvas">
  <section class="card card--front" aria-label="Business card front">
    <div class="brand"><span>Quorvane Advisory</span><span class="brand__dot"></span></div>
    <div class="identity-band">
      <div class="person">
        <p class="person__name">DANIEL HARLOW</p>
        <p class="person__title">CEO/FOUNDER</p>
      </div>
      <ul class="contacts">
        <li class="contacts__item">
          <svg class="contacts__icon" viewBox="0 0 24 24" aria-hidden="true"><path d="M6.6 10.8c1.4 2.8 3.8 5.1 6.6 6.6l2.2-2.2c.3-.3.7-.4 1-.2 1.1.4 2.3.6 3.6.6.6 0 1 .4 1 1V20c0 .6-.4 1-1 1C10.6 21 3 13.4 3 4c0-.6.4-1 1-1h3.5c.6 0 1 .4 1 1 0 1.3.2 2.5.6 3.6.1.3 0 .7-.2 1z"/></svg>
          <span>612 555 0184</span>
        </li>
        <li class="contacts__item">
          <svg class="contacts__icon" viewBox="0 0 24 24" aria-hidden="true"><path d="M2 5h20v2l-10 6L2 7z"/><path d="M2 9l10 6 10-6v10H2z"/></svg>
          <span>info@quorvane.com</span>
        </li>
        <li class="contacts__item">
          <svg class="contacts__icon" viewBox="0 0 24 24" aria-hidden="true"><circle cx="12" cy="12" r="10"/><path d="M12 2c3 3 3 17 0 20M12 2c-3 3-3 17 0 20M2 12h20" fill="none" stroke="#000" stroke-width="1.6"/></svg>
          <span>www.quorvane.com</span>
        </li>
      </ul>
    </div>
    <p class="address">4120 Harbor View Road, Juneau, Alaska 99801</p>
  </section>

  <section class="card card--back" aria-label="Business card back">
    <div class="brand"><span>Quorvane Advisory</span><span class="brand__dot"></span></div>
  </section>
</main>
</body>
</html>
```